washable paper bags and accessories

We are three sisters who have discovered a mutual love of bags made from washable paper. It is a brand new business venture for bags, handbags, cosmetic bags, and home storage solutions and décor all made with washable paper.
We would like to have white crumpled paper as a background for both sides. Front of card with the words "plume douce cloth" only in "bohemian typewriter regular" font. Back of card with appointment style format for our next pop up stall
Target Market(s)
mums, females
Industry/Entity Type
Business
Contact Information for Business Card
ph: 0487215364
email:plumedoucecloth@mailbarrow.com

```html
<!DOCTYPE html>
<html lang="en">
<head>
<meta charset="utf-8">
<title>Plume Douce Cloth – Appointment Card</title>
<link rel="stylesheet" href="https://fonts.googleapis.com/css2?family=Arimo&display=swap">
<style>
  :root {
    --canvas: #ffffff;
    --paper-light: #f1f1ea;
    --paper-mid: #dcdcd2;
    --paper-shade: #cfcfc4;
    --teal: #2bbfa3;
    --teal-soft: #8fd1bf;
    --ink: #111111;
  }
  html, body {
    margin: 0;
    padding: 0;
    width: 1200px;
    height: 1200px;
    overflow: hidden;
    background: var(--canvas);
  }
  .card {
    position: absolute;
    left: 316px;
    top: 130px;
    width: 570px;
    height: 502px;
    overflow: hidden;
    font-family: "Arimo", Arial, sans-serif;
    color: var(--ink);
  }
  .paper-texture {
    position: absolute;
    inset: 0;
    background:
      radial-gradient(circle at 30% 25%, var(--paper-light) 0%, transparent 55%),
      radial-gradient(circle at 75% 70%, var(--paper-light) 0%, transparent 50%),
      linear-gradient(135deg, var(--paper-mid), var(--paper-light) 45%, var(--paper-shade));
  }
  .label-vertical {
    position: absolute;
    font-size: 21px;
    white-space: nowrap;
    transform: translate(-50%, -50%) rotate(-90deg);
  }
  .label-name { left: 41px; top: 130px; }
  .label-time { left: 137px; top: 76px; }
  .label-date { left: 137px; top: 175px; }
  .name-rule {
    position: absolute;
    left: 86px;
    top: 27px;
    width: 3px;
    height: 203px;
    background: var(--teal);
  }
  .schedule {
    position: absolute;
    left: 154px;
    top: 28px;
  }
  .brand {
    position: absolute;
    left: 60px;
    top: 348px;
    display: flex;
    align-items: center;
    gap: 14px;
  }
  .brand-mark {
    width: 22px;
    height: 22px;
    background: var(--teal);
  }
  .brand-name {
    font-family: "Arimo", Arial, sans-serif;
    font-size: 30px;
    font-weight: 400;
    color: var(--ink);
  }
  .contact {
    position: absolute;
    right: 31px;
    top: 420px;
    text-align: right;
    font-size: 22px;
    line-height: 27px;
  }
  .contact p { margin: 0; }
</style>
</head>
<body>
  <main class="card">
    <div class="paper-texture" role="img" aria-label="White crumpled paper texture"></div>

    <span class="label-vertical label-name">Name:</span>
    <div class="name-rule"></div>
    <span class="label-vertical label-time">Time</span>
    <span class="label-vertical label-date">Date</span>

    <svg class="schedule" width="366" height="198" viewBox="0 0 366 198" aria-label="Appointment date and time table">
      <rect x="1" y="1" width="363" height="196" fill="#8fd1bf" stroke="#111" stroke-width="1.5"/>
      <g stroke="#111" stroke-width="1.5">
        <line x1="35" y1="1" x2="35" y2="197"/>
        <line x1="65" y1="1" x2="65" y2="197"/>
        <line x1="95" y1="1" x2="95" y2="197"/>
        <line x1="126" y1="1" x2="126" y2="197"/>
        <line x1="156" y1="1" x2="156" y2="197"/>
        <line x1="186" y1="1" x2="186" y2="197"/>
        <line x1="216" y1="1" x2="216" y2="197"/>
        <line x1="246" y1="1" x2="246" y2="197"/>
        <line x1="276" y1="1" x2="276" y2="197"/>
        <line x1="306" y1="1" x2="306" y2="197"/>
        <line x1="336" y1="1" x2="336" y2="197"/>
        <line x1="4" y1="95" x2="366" y2="92"/>
      </g>
    </svg>

    <div class="brand">
      <span class="brand-mark"></span>
      <span class="brand-name">plume douce cloth</span>
    </div>

    <div class="contact">
      <p>ph: 048-721-5364</p>
      <p>email: plumedoucecloth@mailbarrow.com</p>
    </div>
  </main>
</body>
</html>
```